Psychometric Assessment Flyer/Brochure Makeover

TREV Consulting is an organisational psychology and human resource management consulting firm based in Melbourne, Australia (www.trevadvise.com.au). We offer a range of organisational development and executive recruitment services, however the largest part of our business is our online psychometric assessments portal, which is currently used by hundreds of organisations Australia wide as part of their recruitment process.

We are seeking assistance with the redevelopment of an existing 2-page (1 x A4 page double sided) brochure/flyer to make it more impactful. The main purpose of the brochure is to increase sales revenue in our assessments area. We believe that part of the path to increasing/generating revenue is going to be caused by enquiries made to the business as a result of reading this flyer.

Due to the complex nature of psychometric assessments, the content in this existing brochure attached needs to be simplified and easy to understand. Our target audience are businesses and organisations from a range of sectors (eg. not-for-profit/commercial/local & state government). Feel free if you just want to capture key points also.

Please note, we are not just seeking an aesthetic improvement to the brochure, we are seeking direction on the layout and content also.

Target Market(s)

HR Managers, Recruiters, CEO, General Manager, Mangers of private and not for profit organisations.

Font styles to use
Sans Serif

Requirements
Must have
• Company logo (attached); colours are Dark Blue: R53 G67 B113, White: R255 G255 B 255. TREV Consulting also uses the following colours for corporate branding and communications:
• Dark Blue: R53 G67 B113 = Hex #354371
• Pink: R202 G48 B146 = Hex #CA3092
• Medium Blue: R80 G145 B205 = Hex #5091CD
• Yellow: R231, G166, B20 = Hex #E7A614
• Contact details as specified in attached flyer.

```html
<!DOCTYPE html>
<html lang="en">
<head>
<meta charset="utf-8">
<title>TREV Consulting – Psychometric Assessment</title>
<link rel="stylesheet" href="https://fonts.googleapis.com/css2?family=Exo+2:wght@600;700&family=Open+Sans:wght@400;700&display=swap">
<style>
  :root{
    --page-bg:#e4e4e2;
    --paper:#ffffff;
    --navy:#354371;
    --pink:#ca3092;
    --sky:#0aa2e2;
    --hero-dark:#062636;
    --hero-mid:#0c4257;
    --ink:#2a2a2a;
  }
  *{box-sizing:border-box;margin:0;padding:0}
  html,body{width:1200px;height:1200px;overflow:hidden;background:var(--page-bg)}
  body{font-family:"Open Sans",Arial,sans-serif;color:var(--ink)}
  .flyer{position:absolute;left:151px;top:20px;width:898px;height:1161px;background:var(--paper);box-shadow:0 4px 14px rgba(0,0,0,.18);overflow:hidden}
  .hero{position:absolute;left:0;top:0;width:898px;height:442px;
    background:radial-gradient(ellipse at 72% 40%, var(--hero-mid) 0%, #0a3346 45%, var(--hero-dark) 100%)}
  .brand{position:absolute;left:84px;top:322px;font-family:"Exo 2",sans-serif;font-weight:700;font-size:38px;color:#fff;letter-spacing:.5px}
  .hero-title{position:absolute;left:527px;top:302px;font-family:"Exo 2",sans-serif;font-weight:700;font-size:46px;line-height:50px;color:#fff}
  .intro-heading{position:absolute;left:84px;top:460px;font-family:"Exo 2",sans-serif;font-weight:700;font-size:37px;line-height:40px;color:var(--navy)}
  .body-text{font-size:17.4px;line-height:19.4px;color:var(--ink)}
  .intro-text{position:absolute;left:84px;top:500px;width:740px}
  .intro-tagline{position:absolute;left:84px;top:593px}
  .benefits-band{position:absolute;left:0;top:632px;width:427px;height:41px;background:var(--pink);
    padding-left:83px;font-family:"Exo 2",sans-serif;font-weight:600;font-size:27px;line-height:41px;color:#fff}
  .benefits{position:absolute;left:84px;top:690px;width:352px}
  .benefits ul{list-style:none}
  .benefits li{position:relative;padding-left:17px}
  .benefits li::before{content:"•";position:absolute;left:0;font-size:14px}
  .benefits .turnover{margin-top:19.4px}
  .offer-heading{position:absolute;left:469px;top:638px;font-family:"Exo 2",sans-serif;font-weight:700;font-size:27px;line-height:29px;color:var(--navy)}
  .offer-text{position:absolute;left:469px;top:697px;width:360px}
  .offer-text strong{font-weight:700}
  .assessment-grid{position:absolute;left:469px;top:802px;display:grid;grid-template-columns:169px 169px;grid-auto-rows:59px;gap:5px 5px}
  .assessment{background:var(--sky);color:#fff;display:flex;align-items:center;justify-content:center;text-align:center;font-size:16.5px;line-height:18.5px}
</style>
</head>
<body>
  <article class="flyer">
    <header class="hero" role="img" aria-label="Photo of a person in a dark suit holding out cupped hands with small white people icons floating above them">
      <div class="brand">TREV Consulting</div>
      <h1 class="hero-title">Psychometric<br>Assessment</h1>
    </header>

    <h2 class="intro-heading">Reduce Hiring Mistakes</h2>
    <p class="intro-text body-text">Psychometric Assessments are a powerful and cost-effective way of accurately predicting the likelihood of success of a candidate in any given role. In comparison to traditional recruitment and selection processes such as interviews and reference checking, Psychometric Assessment is evidence based, unbiased and incredibly accurate.</p>
    <p class="intro-tagline body-text">The most accurate predictor of on the job success.</p>

    <h3 class="benefits-band">Benefits of assessment</h3>
    <section class="benefits body-text">
      <p>The use of Psychometric Assessments in a recruitment process has led to substantial and sustained work outcomes including:</p>
      <ul>
        <li>Increased productivity and speed to productivity</li>
        <li>Less negative behaviours in the workplace</li>
        <li>Improved employee engagement</li>
        <li>Less disciplinary action required</li>
        <li>Lower turnover</li>
        <li>Less time invested recruiting and training new employees</li>
        <li>Less money spent on advertising vacancies</li>
        <li>Higher client satisfaction ratings</li>
      </ul>
      <p class="turnover">Please turn over to see a testimonial from Harlow Aged Care outlining the benefits they have experienced since implementing psychometric assessments as part of their recruitment process.</p>
    </section>

    <h3 class="offer-heading">What assessments<br>can I administer?</h3>
    <p class="offer-text body-text">TREV offers a range of <strong>psychometric assessments</strong> designed to measure the likelihood of success at work, as well as potential risk areas. These include:</p>

    <div class="assessment-grid">
      <div class="assessment">Personality</div>
      <div class="assessment">Values</div>
      <div class="assessment">Cognitive Ability</div>
      <div class="assessment">Emotional<br>Intelligence</div>
      <div class="assessment">Resilience</div>
      <div class="assessment">Attitudes Toward<br>Diversity</div>
      <div class="assessment">Engagement</div>
      <div class="assessment">OH&amp;S</div>
      <div class="assessment">Counter-Productive<br>Work Behaviours</div>
    </div>
  </article>
</body>
</html>
```